Northgate Bone Clinic Web
NBC web
Creative Brief
Health
Northgate Bone Clinic is a regional center for treatment spine related problems. We treat all sorts of spine problems including surgery, pain management, physical therapy.
left side
www.corvellaclinic.com
www.tovarix.com
www.brindlemorehealth.com
I will upload our logo with information.

```html
<!DOCTYPE html>
<html lang="en">
<head>
<meta charset="utf-8">
<title>Northgate Bone Clinic</title>
<link href="https://fonts.googleapis.com/css2?family=Arimo:wght@400;700&family=Cinzel:wght@700&display=swap" rel="stylesheet">
<style>
:root{
  --navy:#1c3668;
  --red:#cc1020;
  --ink:#333;
  --muted:#666;
  --band:#ececec;
  --line:#d6d6d6;
  --footer:#2b2b2b;
  --footer-text:#cfcfcf;
  --panel:rgba(255,255,255,.9);
  --white:#fff;
}
*{box-sizing:border-box;margin:0;padding:0}
html,body{width:1200px;height:1062px;overflow:hidden}
body{position:relative;background:var(--white);font-family:"Arimo",Arial,sans-serif;color:var(--ink);font-size:11px}
.abs{position:absolute}
ul{list-style:none}

.topbar{left:0;top:0;width:1200px;height:18px;background:#f4f4f4;border-bottom:1px solid var(--line)}
.toplinks{right:190px;top:0;display:flex;gap:2px}
.toplinks a{background:var(--red);color:var(--white);font-size:9px;padding:3px 6px;text-decoration:none}

.brand{left:175px;top:30px;display:flex;align-items:center;gap:12px}
.brand-mark{width:38px;height:38px;border-radius:50%;background:var(--navy)}
.brand-name{font-family:"Cinzel",serif;font-weight:700;font-size:19px;color:var(--navy);line-height:1.1;width:170px}
.search{left:848px;top:42px;width:152px;height:26px;border:1px solid var(--line);background:var(--white);color:#999;font-size:11px;padding:6px 10px}
.search svg{position:absolute;right:8px;top:6px}
.nav{left:410px;top:80px;display:flex;height:40px}
.nav a{display:block;padding:0 14px;line-height:40px;font-size:14px;color:var(--navy);text-decoration:none;border-right:1px solid var(--line)}
.nav a.active{background:var(--red);color:var(--white)}

.hero{left:0;top:120px;width:1200px;height:340px;background:linear-gradient(90deg,#dfe3e6 0%,#eef1f3 40%,#c9d4de 75%,#9fb4c6 100%)}
.hero-copy{left:400px;top:290px;width:330px;font-family:"Cinzel",serif;font-weight:700;font-size:15px;line-height:1.3;color:var(--navy)}
.hero-copy span{color:var(--red)}
.btn-navy{left:400px;top:366px;background:var(--navy);color:var(--white);font-family:"Cinzel",serif;font-weight:700;font-size:14px;padding:8px 12px}
.dots{left:690px;top:430px;display:flex;gap:4px}
.dots i{width:9px;height:9px;border-radius:50%;background:#999}
.dots i:first-child{background:var(--red)}

.contact{left:763px;top:135px;width:238px;height:290px;background:var(--panel);z-index:5}
.contact h2{background:var(--red);color:var(--white);font-size:15px;text-align:center;height:36px;line-height:36px;letter-spacing:.5px}
.contact form{padding:10px 12px}
.field{height:24px;border:1px solid var(--line);background:var(--white);margin-bottom:7px;font-size:10px;color:#999;padding:5px 8px}
.field.tall{height:52px}
.submit{display:block;margin:4px auto 0;width:130px;height:28px;background:var(--navy);color:var(--white);font-size:15px;font-weight:700;text-align:center;line-height:28px}
.callout{left:763px;top:425px;width:238px;height:82px;z-index:5}
.callout svg{display:block}
.callout-text{left:0;top:6px;width:238px;text-align:center;color:var(--red);font-weight:700;font-size:16px;line-height:1.2}

.band{left:0;top:463px;width:1200px;height:152px;background:var(--band)}
.band-col h3,.col h3{font-family:"Cinzel",serif;font-weight:700;font-size:15px;color:var(--navy);border-bottom:1px solid var(--line);padding-bottom:6px;margin-bottom:8px}
.band-col{top:472px;width:270px}
.bullets li{position:relative;padding-left:14px;font-size:10px;line-height:24px;border-bottom:1px dotted var(--line);width:150px}
.bullets li::before{content:"";position:absolute;left:2px;top:9px;width:6px;height:6px;border-radius:50%;background:var(--navy)}
.round-photo{position:absolute;right:0;top:34px;width:100px;height:100px;border-radius:50%;border:4px solid var(--white)}
.photo-team{background:linear-gradient(160deg,#e9eef3,#b9c8d6)}
.photo-injury{background:linear-gradient(160deg,#f1e4d8,#d2b49a)}
.follow{left:770px;top:510px;width:240px;height:92px;border-left:1px solid var(--line);display:flex;align-items:center;justify-content:flex-end;gap:7px}
.follow strong{font-family:"Cinzel",serif;font-size:14px;color:var(--navy);margin-right:6px;white-space:nowrap}
.follow i{width:26px;height:26px;border-radius:50%;background:var(--navy)}

.col{top:638px;width:258px}
.col p{font-size:10px;line-height:1.45;color:var(--muted)}
.quote{font-family:Georgia,serif;font-size:30px;color:var(--navy);line-height:.7}
.quote.end{text-align:right}
.author{text-align:right;font-size:10px;color:var(--navy);font-weight:700;margin:4px 0 8px}
.news-item{position:relative;border-bottom:1px solid var(--line);padding:5px 30px 6px 0}
.news-item b{font-size:10px;color:var(--ink)}
.news-item .arrow{position:absolute;right:2px;top:12px;width:20px;height:20px;border-radius:50%;background:#bdbdbd}
.news-item .arrow::after{content:"";position:absolute;left:7px;top:6px;border:4px solid transparent;border-left:6px solid var(--white)}
.rehab-photo{float:left;width:60px;height:66px;margin:0 8px 4px 0;background:linear-gradient(160deg,#d6dde3,#8fa3b5)}
.read{font-size:10px;font-weight:700;color:var(--navy);display:block;margin-top:4px}

.footer{left:0;top:880px;width:1200px;height:145px;background:var(--footer)}
.fcol{top:895px;color:var(--footer-text);font-size:10px}
.fcol h4{font-family:"Cinzel",serif;color:var(--white);font-size:14px;margin-bottom:10px}
.sitemap{display:flex;gap:38px}
.sitemap li{line-height:18px;padding-left:10px;position:relative}
.sitemap li::before{content:"";position:absolute;left:0;top:6px;width:4px;height:4px;background:var(--red)}
.contact-col{width:195px}
.contact-list li{display:flex;gap:6px;align-items:flex-start;line-height:14px;margin-bottom:6px}
.contact-list svg{flex:none;margin-top:2px}
.newsletter{width:180px}
.newsletter input{display:block;width:160px;height:22px;border:0;margin:8px 0 6px;padding:0 6px;font-size:10px;color:#888;background:var(--white)}
.signup{display:inline-block;background:var(--red);color:var(--white);font-weight:700;font-size:11px;padding:5px 10px}
.foot-brand{left:870px;top:905px}
.foot-brand .brand-name{display:block;color:var(--white);font-size:16px;width:150px}
.bottom{left:190px;top:1040px;width:820px;display:flex;justify-content:space-between;font-size:9px;color:var(--muted)}
</style>
</head>
<body>
<div class="abs topbar"></div>
<div class="abs toplinks"><a href="#">News</a><a href="#">Blog</a><a href="#">Login</a><a href="#">Register</a></div>

<header>
  <div class="abs brand"><span class="brand-mark"></span><span class="brand-name">Northgate Bone Clinic</span></div>
  <div class="abs search">Search
    <svg width="12" height="12" viewBox="0 0 12 12"><circle cx="5" cy="5" r="3.6" fill="none" stroke="#888" stroke-width="1.6"/><line x1="7.6" y1="7.6" x2="11" y2="11" stroke="#888" stroke-width="1.8"/></svg>
  </div>
  <nav class="abs nav">
    <a class="active" href="#">Home</a><a href="#">Conditions</a><a href="#">Treatments</a><a href="#">About Us</a><a href="#">Our Physicians</a><a href="#">Contact Us</a>
  </nav>
</header>

<section>
  <div class="abs hero" role="img" aria-label="Doctor holding a stethoscope toward the viewer, with a spine illustration on the right"></div>
  <p class="abs hero-copy">We treat all sorts of spine problems including surgery, <span>pain management, physical therapy...</span></p>
  <div class="abs btn-navy">Read More</div>
  <div class="abs dots"><i></i><i></i><i></i><i></i></div>

  <aside class="abs contact">
    <h2>CONTACT REQUEST</h2>
    <form>
      <div class="field">First Name</div>
      <div class="field">Last Name</div>
      <div class="field">Phone</div>
      <div class="field">Email</div>
      <div class="field tall">Messages</div>
      <div class="submit">SUBMIT</div>
    </form>
  </aside>
</section>

<section>
  <div class="abs band"></div>
  <div class="abs band-col" style="left:195px">
    <h3>OUR TEAM</h3>
    <ul class="bullets"><li>Lorem ipsum dolor sit amet</li><li>Lorem ipsum dolor sit amet</li><li>Lorem ipsum dolor sit amet</li><li>Lorem ipsum dolor sit amet</li></ul>
    <div class="round-photo photo-team" role="img" aria-label="Smiling doctor in a white coat"></div>
  </div>
  <div class="abs band-col" style="left:485px">
    <h3>INJURY</h3>
    <ul class="bullets"><li>Lorem ipsum dolor sit amet</li><li>Lorem ipsum dolor sit amet</li><li>Lorem ipsum dolor sit amet</li><li>Lorem ipsum dolor sit amet</li></ul>
    <div class="round-photo photo-injury" role="img" aria-label="Person holding their aching lower back"></div>
  </div>
  <div class="abs follow"><strong>FOLLOW US:</strong><i></i><i></i><i></i><i></i></div>

  <div class="abs callout">
    <svg width="238" height="82" viewBox="0 0 238 82"><path d="M0 0H238V46L119 82L0 46Z" fill="rgba(255,255,255,.95)"/></svg>
    <div class="abs callout-text">CALL TODAY<br>(000) 000 0000</div>
  </div>
</section>

<main>
  <div class="abs col" style="left:192px">
    <h3>TESTIMONIAL</h3>
    <div class="quote">&ldquo;</div>
    <p>Lorem ipsum dolor sit amet, consectetur adipiscing elit sed do eiusmod tempor incididunt ut labore et dolore magna aliqua.</p>
    <div class="author">Lorem Ipsum Dolor</div>
    <p>Lorem ipsum dolor sit amet, consectetur adipiscing elit sed do eiusmod tempor incididunt ut labore et dolore.</p>
    <div class="author">Lorem Ipsum Dolor</div>
    <div class="quote end">&rdquo;</div>
  </div>
  <div class="abs col" style="left:468px">
    <h3>LATEST NEWS</h3>
    <div class="news-item"><b>2013-06-04 | Lorem ipsum dolor sit</b><p>Lorem ipsum dolor sit amet, consectetur sed do eiusmod tempor incididunt</p><span class="arrow"></span></div>
    <div class="news-item"><b>2013-06-06 | Lorem ipsum dolor sit</b><p>Lorem ipsum dolor sit amet, consectetur sed do eiusmod tempor incididunt</p><span class="arrow"></span></div>
    <div class="news-item"><b>2013-06-08 | Lorem ipsum dolor sit</b><p>Lorem ipsum dolor sit amet, consectetur sed do eiusmod tempor incididunt</p><span class="arrow"></span></div>
  </div>
  <div class="abs col" style="left:752px">
    <h3>REHABILITATION</h3>
    <div class="rehab-photo" role="img" aria-label="Physical therapist guiding a patient through exercise"></div>
    <p>Lorem ipsum dolor sit amet, consectetur adipiscing elit sed do eiusmod tempor incididunt ut labore et dolore magna aliqua ut enim ad minim veniam quis nostrud.</p>
    <p style="margin-top:8px;clear:both">Ut enim ad minim veniam quis nostrud exercitation ullamco laboris nisi ut aliquip ex ea commodo consequat duis aute irure dolor in reprehenderit in voluptate velit esse.</p>
    <span class="read">Read More</span>
  </div>
</main>

<footer>
  <div class="abs footer"></div>
  <div class="abs fcol" style="left:192px">
    <h4>SITE MAP</h4>
    <div class="sitemap">
      <ul><li>Home</li><li>Conditions</li><li>Treatments</li><li>About Us</li></ul>
      <ul><li>Our Physicians</li><li>News</li><li>Blog</li><li>Contact Us</li></ul>
    </div>
  </div>
  <div class="abs fcol contact-col" style="left:445px">
    <h4>CONTACT US</h4>
    <ul class="contact-list">
      <li><svg width="10" height="10" viewBox="0 0 10 10"><path d="M2 0L4 2.5L3 4Q4.5 6.5 6 7L7.5 6L10 8L8.5 10Q3 9 0 1.5Z" fill="#cfcfcf"/></svg><span><b>Phone:</b> (000) 000 0000</span></li>
      <li><svg width="10" height="8" viewBox="0 0 10 8"><rect x="0" y="0" width="10" height="8" fill="#cfcfcf"/><path d="M0 0L5 4.5L10 0" stroke="#2b2b2b" fill="none"/></svg><span><b>Email:</b> info@northgatebone.org</span></li>
      <li><svg width="10" height="12" viewBox="0 0 10 12"><path d="M5 12Q0 6 0 5A5 5 0 0 1 10 5Q10 6 5 12Z" fill="#cfcfcf"/><circle cx="5" cy="5" r="1.8" fill="#2b2b2b"/></svg><span><b>Address:</b> Lorem ipsum dolor sit amet, consectetur</span></li>
    </ul>
  </div>
  <div class="abs fcol newsletter" style="left:660px">
    <h4>NEWSLETTER</h4>
    <p>Lorem ipsum dolor sit amet, consect</p>
    <input type="text" value="Enter Your Mail" aria-label="Email address">
    <span class="signup">Signup</span>
  </div>
  <div class="abs foot-brand"><span class="brand-name">Northgate Bone Clinic</span></div>
  <div class="abs bottom"><span>Privacy Policy</span><span>Copyright 2013</span></div>
</footer>
</body>
</html>
```